LA's Newest MIRA Facial Oil and Body Oil Packaging Project

We need a packaging concept for a Hemp based facial oil and body oil. We need label design for the bottle and carton graphics. I am attaching a few reference photos. The target demographic is women between 17-35 year old. Products need to be able to stand out in crowded stores with clear calls to action.
1oz Dropper Bottle with Unit Carton - Hemp Facial Oil
4oz PET Bottle with Unit Carton - Hemp + Rose Facial Oil

```html
<!DOCTYPE html>
<html lang="en">
<head>
<meta charset="utf-8">
<title>Mira Body Oil and Face Oil Packaging</title>
<link rel="stylesheet" href="https://fonts.googleapis.com/css2?family=Cinzel:wght@400;500&family=Italianno&family=Arimo:wght@700&display=swap">
<style>
  :root {
    --paper: #ffffff;
    --cream: #f0dfbf;
    --label-gold-light: #f3e6c8;
    --label-gold-dark: #dcc597;
    --pattern-brown: #6b3b1c;
    --pattern-brown-light: #7a4224;
    --brand-brown: #8e4a1f;
    --script-brown: #7a4a22;
    --band-pink: #d6197a;
    --band-text: #ffffff;
    --ink: #1d1d1d;
  }
  * { box-sizing: border-box; margin: 0; padding: 0; }
  html, body { width: 1200px; height: 1000px; overflow: hidden; background: var(--paper); }
  .canvas { position: relative; width: 1200px; height: 1000px; background: var(--paper); }

  .panel {
    position: absolute;
    background: var(--cream);
    display: flex;
    flex-direction: column;
    align-items: center;
    text-align: center;
    overflow: hidden;
  }
  .label { background: linear-gradient(180deg, var(--label-gold-light), var(--label-gold-dark)); }

  .floral-pattern {
    width: 100%;
    flex: none;
    background: radial-gradient(circle at 50% 50%, var(--pattern-brown-light), var(--pattern-brown));
  }
  .brand-name {
    font-family: "Cinzel", serif;
    font-weight: 500;
    color: var(--brand-brown);
    letter-spacing: 0.06em;
    line-height: 1;
  }
  .product-name {
    font-family: "Italianno", cursive;
    color: var(--script-brown);
    line-height: 1;
  }
  .ingredient-band {
    width: 100%;
    flex: none;
    background: var(--band-pink);
    color: var(--band-text);
    font-family: "Cinzel", serif;
    display: flex;
    align-items: center;
    justify-content: center;
    line-height: 1.2;
  }
  .skin-types {
    font-family: "Cinzel", serif;
    color: var(--brand-brown);
    letter-spacing: 0.03em;
    line-height: 1;
  }
  .volume {
    font-family: "Arimo", sans-serif;
    font-weight: 700;
    color: var(--ink);
    line-height: 1;
  }

  /* Body oil carton */
  .body-carton { left: 100px; top: 120px; width: 276px; height: 746px; }
  .body-carton .floral-pattern { height: 315px; }
  .body-carton .brand-name { font-size: 68px; margin-top: 34px; }
  .body-carton .product-name { font-size: 60px; margin-top: 40px; }
  .body-carton .ingredient-band { height: 75px; font-size: 19px; margin-top: 34px; }
  .body-carton .skin-types { font-size: 18px; margin-top: 26px; }
  .body-carton .volume { font-size: 15px; margin-top: 27px; }

  /* Body oil bottle label */
  .body-label { left: 405px; top: 510px; width: 230px; height: 300px; }
  .body-label .floral-pattern { height: 100px; }
  .body-label .brand-name { font-size: 48px; margin-top: 15px; }
  .body-label .product-name { font-size: 40px; margin-top: 3px; }
  .body-label .ingredient-band { height: 55px; font-size: 15px; margin-top: 6px; }
  .body-label .skin-types { font-size: 12px; margin-top: 7px; }
  .body-label .volume { font-size: 9px; margin-top: 5px; }

  /* Face oil carton */
  .face-carton { left: 693px; top: 243px; width: 240px; height: 619px; }
  .face-carton .floral-pattern { height: 247px; }
  .face-carton .brand-name { font-size: 58px; margin-top: 24px; }
  .face-carton .product-name { font-size: 52px; margin-top: 28px; }
  .face-carton .ingredient-band { height: 66px; font-size: 18px; margin-top: 28px; }
  .face-carton .skin-types { font-size: 15px; margin-top: 27px; }
  .face-carton .volume { font-size: 14px; margin-top: 36px; }

  /* Face oil bottle label */
  .face-label { left: 958px; top: 605px; width: 164px; height: 232px; }
  .face-label .floral-pattern { height: 60px; }
  .face-label .brand-name { font-size: 36px; margin-top: 13px; }
  .face-label .product-name { font-size: 32px; margin-top: 7px; }
  .face-label .ingredient-band { height: 38px; font-size: 11px; margin-top: 6px; }
  .face-label .skin-types { font-size: 11px; margin-top: 5px; }
  .face-label .volume { font-size: 8px; margin-top: 4px; }
</style>
</head>
<body>
<main class="canvas">

  <section class="panel body-carton">
    <div class="floral-pattern" role="img" aria-label="Repeating pattern of pink and coral roses and lotus flowers on brown"></div>
    <h1 class="brand-name">MIRA</h1>
    <p class="product-name">Body Oil</p>
    <p class="ingredient-band">With Hemp Oil<br>and Rose Petals</p>
    <p class="skin-types">ALL SKIN TYPES</p>
    <p class="volume">4 fl. Oz 30ml</p>
  </section>

  <section class="panel label body-label">
    <div class="floral-pattern" role="img" aria-label="Repeating pattern of pink and coral roses and lotus flowers on brown"></div>
    <h2 class="brand-name">MIRA</h2>
    <p class="product-name">Body Oil</p>
    <p class="ingredient-band">With Hemp Oil<br>and Rose Petals</p>
    <p class="skin-types">ALL SKIN TYPES</p>
    <p class="volume">4 fl. Oz 30ml</p>
  </section>

  <section class="panel face-carton">
    <div class="floral-pattern" role="img" aria-label="Repeating pattern of pink and coral roses and lotus flowers on brown"></div>
    <h2 class="brand-name">MIRA</h2>
    <p class="product-name">Face Oil</p>
    <p class="ingredient-band">With Hemp Oil<br>and Rose</p>
    <p class="skin-types">ALL SKIN TYPES</p>
    <p class="volume">1 fl. Oz 30ml</p>
  </section>

  <section class="panel label face-label">
    <div class="floral-pattern" role="img" aria-label="Repeating pattern of pink and coral roses and lotus flowers on brown"></div>
    <h2 class="brand-name">MIRA</h2>
    <p class="product-name">Face Oil</p>
    <p class="ingredient-band">With Hemp Oil<br>and Rose</p>
    <p class="skin-types">ALL SKIN TYPES</p>
    <p class="volume">1fl.Oz30ml</p>
  </section>

</main>
</body>
</html>
```